Our company name is VERANTIS FUND PARTNERS. We need a business card for a start up company located in Medellin Colombia. The company will also be shortly expanding to USA. We are a Biotech company responsible for funding regenerative medicine projects with an emphasis on stem cell treatment and regeneration clinics. This will be a global company so the final design should communicate world wide financing for the new generation of regenerative medicine.

```html
<!DOCTYPE html>
<html lang="en">
<head>
<meta charset="utf-8">
<title>Verantis Fund Partners – Business Card</title>
<link rel="stylesheet" href="https://fonts.googleapis.com/css2?family=Jost:wght@400;500&display=swap">
<style>
  :root {
    --page-bg: #ece9ee;
    --card-white: #ffffff;
    --brand-purple: #7e1072;
    --accent-teal: #2f9c8b;
    --text-grey: #6d6d72;
    --text-light: #ffffff;
  }
  html, body {
    margin: 0;
    padding: 0;
    width: 1200px;
    height: 1000px;
    overflow: hidden;
    background: var(--page-bg);
  }
  .canvas {
    position: relative;
    width: 1200px;
    height: 1000px;
    font-family: "Jost", "Futura", sans-serif;
  }
  .business-card {
    position: absolute;
    left: 100px;
    top: 214px;
    width: 1000px;
    height: 571px;
    background: var(--card-white);
    overflow: hidden;
    box-shadow: 0 10px 30px rgba(60, 20, 60, 0.15);
  }
  .card-wave {
    position: absolute;
    inset: 0;
    width: 100%;
    height: 100%;
  }
  .wave-fill { fill: var(--brand-purple); }
  .wave-line {
    fill: none;
    stroke: var(--accent-teal);
    stroke-width: 7;
    stroke-linecap: round;
  }
  .company-name {
    position: absolute;
    left: 78px;
    top: 52px;
    margin: 0;
    color: var(--brand-purple);
    font-weight: 500;
    line-height: 1;
  }
  .company-name .name-main {
    display: block;
    font-size: 64px;
    letter-spacing: 1px;
  }
  .company-name .name-sub {
    display: block;
    font-size: 34px;
    margin-top: 4px;
    padding-left: 150px;
  }
  .contact-list {
    position: absolute;
    left: 80px;
    top: 218px;
    margin: 0;
    padding: 0;
    list-style: none;
    color: var(--text-grey);
    font-size: 21px;
    font-weight: 400;
    line-height: 1.45;
    letter-spacing: 0.5px;
  }
  .contact-label {
    display: inline-block;
    width: 22px;
    color: var(--brand-purple);
  }
  .person {
    position: absolute;
    left: 580px;
    top: 318px;
    color: var(--text-light);
  }
  .person-name {
    margin: 0;
    font-size: 33px;
    font-weight: 400;
    letter-spacing: 0.5px;
  }
  .person-title {
    margin: 6px 0 0;
    font-size: 25px;
    font-weight: 500;
    letter-spacing: 0.5px;
  }
</style>
</head>
<body>
<main class="canvas">
  <article class="business-card">
    <svg class="card-wave" viewBox="0 0 1000 571" preserveAspectRatio="none" aria-hidden="true">
      <path class="wave-fill" d="M1000 70 C880 90 820 190 700 240 C560 300 470 390 445 571 L1000 571 Z"/>
      <path class="wave-line" d="M1000 44 C870 70 805 172 688 220 C560 270 478 340 438 470"/>
    </svg>

    <h1 class="company-name">
      <span class="name-main">VERANTIS</span>
      <span class="name-sub">Fund Partners</span>
    </h1>

    <ul class="contact-list">
      <li><span class="contact-label">t</span>(604)555-0183</li>
      <li><span class="contact-label">e</span>m.alder@verantisfund.com</li>
    </ul>

    <div class="person">
      <p class="person-name">Marco Alder</p>
      <p class="person-title">Managing Director</p>
    </div>
  </article>
</main>
</body>
</html>
```